dsadasdasdasdsa

Industry/Entity Type

Mortgage Broking

Requirements
Must have
• Call-to-action button somewhere on the graphic
Nice to have
• The font of our logo is Montserrat

```html
<!DOCTYPE html>
<html lang="en">
<head>
<meta charset="utf-8">
<title>Need a Mortgage Broker? Banner</title>
<link rel="stylesheet" href="https://fonts.googleapis.com/css2?family=Montserrat:wght@800;900&family=Open+Sans:wght@600&display=swap">
<style>
  :root {
    --stage: #c4c5c4;
    --forest: #124c30;
    --headline: #14512f;
    --panel: #efefee;
    --cta-red: #c33a2c;
    --cta-shadow: #7d1f17;
    --cta-text: #ffffff;
    --turtle-shell: #9a5a2c;
    --turtle-skin: #6cc24a;
  }
  * { box-sizing: border-box; margin: 0; padding: 0; }
  html, body {
    width: 1200px;
    height: 957px;
    overflow: hidden;
  }
  body {
    background: var(--stage);
    position: relative;
  }
  .banner {
    position: absolute;
    left: 30px;
    top: 394px;
    width: 1140px;
    height: 168px;
    background: var(--forest);
    overflow: hidden;
  }
  .banner__panel {
    position: absolute;
    left: 80px;
    top: 0;
    width: 640px;
    height: 168px;
    background: var(--panel);
  }
  .mascot {
    position: absolute;
    border-radius: 46% 46% 18% 18%;
    background: linear-gradient(160deg, var(--turtle-skin) 0%, #4f9a39 45%, var(--turtle-shell) 100%);
  }
  .mascot--left   { left: 84px;  top: 2px; width: 100px; height: 166px; }
  .mascot--centre { left: 502px; top: 8px; width: 146px; height: 160px; }
  .mascot--right  { left: 972px; top: 4px; width: 140px; height: 164px; }
  .headline {
    position: absolute;
    z-index: 2;
    left: 219px;
    top: 18px;
    font-family: "Montserrat", sans-serif;
    font-weight: 900;
    font-size: 42px;
    line-height: 46px;
    letter-spacing: -1px;
    white-space: nowrap;
    color: var(--headline);
    text-transform: uppercase;
  }
  .cta {
    position: absolute;
    z-index: 1;
    left: 644px;
    top: 0;
    width: 340px;
    height: 168px;
    display: block;
    text-decoration: none;
  }
  .cta__shape {
    position: absolute;
    inset: 0;
  }
  .cta__label {
    position: absolute;
    left: 26px;
    top: 34px;
    width: 300px;
    text-align: center;
    font-family: "Open Sans", sans-serif;
    font-weight: 600;
    font-size: 22px;
    line-height: 31px;
    letter-spacing: 1.8px;
    white-space: nowrap;
    color: var(--cta-text);
  }
</style>
</head>
<body>
  <section class="banner" aria-label="Need a mortgage broker? Search now on Australia's largest directory">
    <div class="banner__panel"></div>
    <div class="mascot mascot--left" role="img" aria-label="Cartoon turtle mascot waving"></div>
    <div class="mascot mascot--centre" role="img" aria-label="Smiling cartoon turtle mascot"></div>
    <h1 class="headline">Need a<br>Mortgage<br>Broker?</h1>
    <a class="cta" href="#search">
      <svg class="cta__shape" width="340" height="168" viewBox="0 0 340 168" aria-hidden="true">
        <ellipse cx="168" cy="84" rx="168" ry="84" fill="var(--cta-shadow)"/>
        <ellipse cx="180" cy="82" rx="154" ry="78" fill="var(--cta-red)"/>
      </svg>
      <span class="cta__label">Search Now on<br>Australia's Largest<br>Directory</span>
    </a>
    <div class="mascot mascot--right" role="img" aria-label="Cartoon turtle mascot pointing at the button"></div>
  </section>
</body>
</html>
```